Family Ranch with a hobby vineyard needs 2 wine labels for our first harvest

Design 2 wine labels (front and back) with the Morvasco Ranch logo.
Label 1:
Sauvignon Blanc
Alc. 12.5% by Vol.
Palos Verdes Peninsula - add as the region
Year 2022
Label 2:
Cabernet Sauvignon
Alc. 13.5% by Vol.
Year 2022
For the back label design:
GOVERNMENT WARNING: (1) According to the Surgeon General, women
should not drink alcoholic beverages during pregnancy because of the risk of
birth defects. (2) Consumption of alcoholic beverages impairs your ability to
drive a car or operate machinery, and may cause health problems.
Contains Sulfates.
750ML
I just received the bottles and have attached a picture.

```html
<!DOCTYPE html>
<html lang="en">
<head>
<meta charset="utf-8">
<title>Morvasco Ranch – Wine Labels 2022</title>
<link rel="stylesheet" href="https://fonts.googleapis.com/css2?family=Lato:wght@400;700&family=Pinyon+Script&display=swap">
<style>
  :root {
    --canvas-bg: #ffffff;
    --label-bg: #f3f3f1;
    --label-edge: #e2e2df;
    --ink: #141414;
    --brand: #3a3a3a;
    --gold: #b8963f;
    --red: #a3262a;
    --script: #9a9a9a;
    --sketch-light: #eeeeec;
    --sketch-dark: #b9b9b6;
  }
  * { box-sizing: border-box; margin: 0; padding: 0; }
  html, body {
    width: 910px; height: 1200px; overflow: hidden;
    background: var(--canvas-bg);
  }
  .canvas {
    position: relative; width: 910px; height: 1200px;
    display: flex; justify-content: center; align-items: center; gap: 30px;
  }
  .label {
    position: relative; width: 410px; height: 441px;
    background: linear-gradient(90deg, #fafaf8 0%, var(--label-bg) 55%, var(--label-edge) 100%);
    font-family: "Lato", sans-serif;
    color: var(--ink);
  }
  .brand {
    position: absolute; top: 64px; left: 0; right: 0;
    display: flex; justify-content: center; align-items: center; gap: 8px;
  }
  .brand-dot {
    width: 14px; height: 14px; border-radius: 50%; background: var(--gold);
  }
  .brand-name {
    font-family: "Lato", sans-serif; font-weight: 400;
    font-size: 17px; letter-spacing: 1.5px; color: var(--brand);
    text-transform: uppercase;
  }
  .scene {
    position: absolute; top: 136px; left: 76px; width: 285px; height: 152px;
    background: radial-gradient(ellipse at 40% 75%, var(--sketch-dark) 0%, var(--sketch-light) 60%, transparent 80%);
  }
  .varietal {
    position: absolute; top: 310px; left: 0; right: 0;
    font-weight: 700; font-size: 27px; letter-spacing: 2.5px;
    line-height: 27px; text-transform: uppercase;
  }
  .varietal .line { display: flex; align-items: baseline; white-space: nowrap; }
  .vintage {
    font-weight: 400; font-size: 15px; letter-spacing: 1px; margin-left: 4px;
  }
  .label--red .vintage { color: var(--red); }
  .label--white .vintage { color: var(--gold); }
  .label--red .line--first { padding-left: 100px; }
  .label--red .line--second { padding-left: 118px; }
  .label--white .line--first { padding-left: 87px; }
  .label--white .line--second { padding-left: 87px; }
  .rule {
    display: inline-block; width: 120px; height: 1px; background: var(--gold);
    margin-right: 6px; align-self: center;
  }
  .region {
    position: absolute; top: 383px; left: 0; right: 0; text-align: center;
    font-family: "Pinyon Script", cursive; font-size: 25px; color: var(--script);
    letter-spacing: 1px;
  }
</style>
</head>
<body>
<main class="canvas">
  <section class="label label--red">
    <div class="brand"><span class="brand-dot"></span><span class="brand-name">Morvasco Ranch</span></div>
    <div class="scene" role="img" aria-label="Ink sketch of a lighthouse on rocky coastal cliffs above the sea"></div>
    <h2 class="varietal">
      <span class="line line--first">Cabernet<span class="vintage">2022</span></span>
      <span class="line line--second">Sauvignon</span>
    </h2>
    <p class="region">Palos Verdes Peninsula</p>
  </section>
  <section class="label label--white">
    <div class="brand"><span class="brand-dot"></span><span class="brand-name">Morvasco Ranch</span></div>
    <div class="scene" role="img" aria-label="Ink sketch of a lighthouse on rocky coastal cliffs above the sea"></div>
    <h2 class="varietal">
      <span class="line line--first">Sauvignon<span class="vintage">2022</span></span>
      <span class="line line--second"><span class="rule"></span>Blanc</span>
    </h2>
    <p class="region">Palos Verdes Peninsula</p>
  </section>
</main>
</body>
</html>
```